Halvorsen Partners Business Card

Halvorsen Partners Civil Construction
Marcus Halvorsen
CEO
727-518-6094
Marcus@HalvorsenSiteworks.example
www.HalvorsenSiteworks.example
Site Development
Utility Construction
Excavation
40876 County Lane 19
Cedar Hollow, FL 34719

Target Market(s)

Construction and government

Industry/Entity Type

Business

Contact Information for Business Card

I want an unique design that make a statement

Number of Pages Required

1 page

Font styles to use

Colors

Designer to choose colors to be used in the design.

Requirements
Must have
• unique design, feel free to modify or change the color of my logo.
Nice to have
• extra design features like spot UV, foil accents, color edges, unique paper, or any thing that would make my card pop.
• I like the feel of the image that I attached

```html
<!DOCTYPE html>
<html lang="en">
<head>
<meta charset="utf-8">
<title>Halvorsen Partners Business Card</title>
<link href="https://fonts.googleapis.com/css2?family=Source+Sans+3:wght@400;600;700&display=swap" rel="stylesheet">
<style>
  :root {
    --page-bg: #1c1d1d;
    --card-dark: #2c302f;
    --card-mid: #4a4f4d;
    --card-light: #5d6361;
    --ink-white: #f2f3f2;
    --ink-soft: #d6d9d8;
    --accent-blue: #3d57c9;
    --silhouette: #121414;
  }
  * { box-sizing: border-box; margin: 0; padding: 0; }
  html, body { width: 1200px; height: 900px; overflow: hidden; }
  body {
    background: var(--page-bg);
    font-family: "Source Sans 3", "Myriad Pro", sans-serif;
    color: var(--ink-white);
    position: relative;
  }
  .card {
    position: absolute;
    left: 280px;
    width: 640px;
    height: 366px;
    overflow: hidden;
    background:
      linear-gradient(178deg, rgba(255,255,255,0.05) 0%, rgba(255,255,255,0) 30%, rgba(255,255,255,0.04) 55%, rgba(0,0,0,0.15) 100%),
      linear-gradient(100deg, var(--card-mid) 0%, var(--card-light) 45%, var(--card-dark) 100%);
    box-shadow: 0 18px 40px rgba(0,0,0,0.55);
  }
  .card--front { top: 50px; }
  .card--back { top: 484px; }

  /* front */
  .brand-lockup {
    position: absolute;
    left: 170px;
    top: 136px;
    display: flex;
    align-items: center;
    gap: 14px;
  }
  .brand-square {
    width: 44px;
    height: 44px;
    border: 3px solid var(--ink-white);
    flex: none;
  }
  .brand-divider {
    width: 1.5px;
    height: 50px;
    background: var(--ink-white);
  }
  .brand-text { display: flex; flex-direction: column; line-height: 1; }
  .brand-name {
    font-weight: 700;
    font-size: 27px;
    letter-spacing: 0.5px;
    text-transform: uppercase;
  }
  .brand-sub-line {
    font-weight: 400;
    font-size: 13px;
    letter-spacing: 3.4px;
    text-transform: uppercase;
    margin-top: 5px;
    color: var(--ink-soft);
  }
  .services {
    position: absolute;
    left: 58px;
    bottom: 40px;
    display: flex;
    gap: 14px;
    list-style: none;
    font-size: 14px;
    letter-spacing: 0.6px;
    color: var(--ink-soft);
  }
  .services li::before { content: "•"; margin-right: 8px; }

  /* back */
  .back-mark {
    position: absolute;
    right: 34px;
    top: 34px;
    display: flex;
    align-items: center;
    gap: 10px;
    font-weight: 700;
    font-size: 19px;
    letter-spacing: 0.5px;
    text-transform: uppercase;
  }
  .back-mark .brand-square { width: 34px; height: 34px; }
  .site-silhouette {
    position: absolute;
    right: 0;
    bottom: 0;
    width: 260px;
    height: 190px;
    background: radial-gradient(ellipse 100% 90% at 100% 100%, var(--silhouette) 0%, rgba(18,20,20,0.75) 45%, rgba(18,20,20,0) 100%);
  }
  .contact {
    position: absolute;
    left: 40px;
    bottom: 30px;
  }
  .person { display: flex; align-items: baseline; gap: 8px; }
  .person-name { font-weight: 600; font-size: 24px; }
  .person-role {
    font-size: 16px;
    border-left: 1.5px solid var(--ink-white);
    padding-left: 8px;
  }
  .accent-rule {
    width: 42px;
    height: 3px;
    background: var(--accent-blue);
    margin: 10px 0 12px;
  }
  .contact-lines { font-size: 15px; color: var(--ink-soft); line-height: 1.55; }
  .contact-row { display: flex; gap: 18px; }
  .contact-item { display: flex; align-items: center; gap: 6px; }
  .contact-item svg { width: 11px; height: 11px; fill: var(--accent-blue); flex: none; }
</style>
</head>
<body>

  <section class="card card--front" aria-label="Card front">
    <div class="brand-lockup">
      <div class="brand-square"></div>
      <div class="brand-divider"></div>
      <div class="brand-text">
        <span class="brand-name">Halvorsen Partners</span>
        <span class="brand-sub-line">Civil Construction</span>
      </div>
    </div>
    <ul class="services">
      <li>Site Development</li>
      <li>Utility Construction</li>
      <li>Excavation</li>
    </ul>
  </section>

  <section class="card card--back" aria-label="Card back">
    <div class="back-mark">
      <div class="brand-square"></div>
      <span>Halvorsen Partners</span>
    </div>
    <div class="site-silhouette" role="img" aria-label="Dark silhouette of an excavator on a dirt mound at the job site"></div>
    <div class="contact">
      <div class="person">
        <span class="person-name">Marcus Halvorsen</span>
        <span class="person-role">CEO</span>
      </div>
      <div class="accent-rule"></div>
      <div class="contact-lines">
        <div>40876 County Lane 19, Cedar Hollow, FL 34719</div>
        <div class="contact-row">
          <span class="contact-item">
            <svg viewBox="0 0 12 12" aria-hidden="true"><path d="M2.5 0.5 L4.5 0.5 L5.5 3 L4 4.2 C4.8 5.8 6.2 7.2 7.8 8 L9 6.5 L11.5 7.5 L11.5 9.5 C11.5 10.6 10.6 11.5 9.5 11.5 C4.5 11 1 7.5 0.5 2.5 C0.5 1.4 1.4 0.5 2.5 0.5 Z"/></svg>
            727-518-6094
          </span>
          <span class="contact-item">
            <svg viewBox="0 0 12 12" aria-hidden="true"><path d="M0.5 2 H11.5 V10 H0.5 Z M1.2 2.6 L6 6.4 L10.8 2.6 Z" fill-rule="evenodd"/></svg>
            Marcus@HalvorsenSiteworks.example
          </span>
        </div>
        <div class="contact-item">
          <svg viewBox="0 0 12 12" aria-hidden="true"><circle cx="6" cy="6" r="5.5"/></svg>
          www.HalvorsenSiteworks.example
        </div>
      </div>
    </div>
  </section>

</body>
</html>
```